Buisness cards for international property developer
Morelli Costruzioni Group
Professional
Beatrice Solange Morelli
CEO
Head Office: Via Campo Lungo 158 00149 Rome Italy
beatrice.morelli@morellicostruzionigroup.com
www.morellicostruzionigroup.com

```html
<!DOCTYPE html>
<html lang="en">
<head>
<meta charset="utf-8">
<title>Morelli Costruzioni Group – Business Cards</title>
<link rel="stylesheet" href="https://fonts.googleapis.com/css2?family=Cinzel:wght@400;700&family=Libre+Baskerville:wght@400;700&display=swap">
<style>
  :root {
    --page: #e9e7e3;
    --card: #ffffff;
    --gold: #c8922a;
    --gold-deep: #a9761c;
    --ink: #2a2622;
    --band: #2b2b2b;
    --band-text: #d8d2c6;
  }
  * { box-sizing: border-box; margin: 0; padding: 0; }
  html, body { width: 1200px; height: 901px; overflow: hidden; }
  body {
    background: var(--page);
    display: flex;
    align-items: center;
    justify-content: center;
    gap: 60px;
    font-family: "Libre Baskerville", Georgia, serif;
    color: var(--ink);
  }
  .card {
    width: 520px;
    height: 300px;
    background: var(--card);
    box-shadow: 0 6px 18px rgba(0,0,0,0.18);
    position: relative;
    overflow: hidden;
  }
  /* Front */
  .card-front { display: flex; flex-direction: column; }
  .front-body { flex: 1; position: relative; }
  .brand {
    position: absolute;
    top: 30px; left: 34px;
    width: 260px;
    display: flex; flex-direction: column; align-items: center; gap: 9px;
  }
  .brand-square {
    width: 62px; height: 44px;
    background: var(--gold);
  }
  .brand-name {
    font-family: "Cinzel", "Times New Roman", serif;
    font-size: 10px;
    letter-spacing: 1.2px;
    color: var(--gold-deep);
    text-transform: uppercase;
    white-space: nowrap;
  }
  .person {
    position: absolute;
    top: 150px; left: 34px;
  }
  .person-name {
    font-weight: 700;
    font-size: 15px;
    color: var(--ink);
  }
  .person-role {
    font-size: 12px;
    margin-top: 4px;
    color: var(--ink);
  }
  .divider {
    position: absolute;
    top: 118px; left: 316px;
    width: 9px; height: 58px;
    background: var(--gold);
  }
  .office {
    position: absolute;
    top: 112px; left: 342px;
    font-size: 12px;
    font-weight: 700;
    font-style: normal;
    line-height: 1.45;
    white-space: nowrap;
  }
  .contact-band {
    height: 30px;
    background: var(--band);
    display: flex; align-items: center; justify-content: space-between;
    padding: 0 22px;
    font-size: 9px;
    color: var(--band-text);
    letter-spacing: 0.3px;
  }
  .edge-stripe { height: 10px; background: var(--gold); }
  /* Back */
  .card-back { padding: 18px; }
  .back-pattern {
    width: 100%; height: 100%;
    background: linear-gradient(135deg, #f3e3c2 0%, #e2b865 50%, #f3e3c2 100%);
    border: 3px solid var(--gold);
  }
</style>
</head>
<body>
  <section class="card card-front" aria-label="Business card front">
    <div class="front-body">
      <div class="brand">
        <div class="brand-square"></div>
        <div class="brand-name">Morelli Costruzioni Group</div>
      </div>
      <div class="person">
        <div class="person-name">Beatrice Solange Morelli</div>
        <div class="person-role">CEO</div>
      </div>
      <div class="divider"></div>
      <address class="office">
        Head Office:<br>
        Via Campo Lungo 158<br>
        00149 Rome<br>
        Italy
      </address>
    </div>
    <div class="contact-band">
      <span class="contact-email">beatrice.morelli@morellicostruzionigroup.com</span>
      <span class="contact-web">www.morellicostruzionigroup.com</span>
    </div>
    <div class="edge-stripe"></div>
  </section>

  <section class="card card-back" aria-label="Business card back">
    <div class="back-pattern" role="img" aria-label="Repeating gold brand-monogram pattern covering the card back"></div>
  </section>
</body>
</html>
```